a Label for a candle jar and its gift box

I would like a label that is modern minimalist for candles jars. These jars are colored as white, amber and black. I am thinking maybe foiling gold/silver background with logo only and maybe company name in different color that suits the foiling background color/s. I would like a high quality luxurious design that shows the preciousness of this candle. I am open to any ideas you might have for the design but so far I have used a logo only on the jar which I really like BUT I still feel that it is not enough branding for people when you only show them the logo so I am considering adding the business name. Again, I am open to both ideas (with logo only or logo with business name (Silken Meadow).

IMPORTANT: YOU MAY IGNORE MY DESIGN COMPLETELY AND DO YOUR OWN ONE AS LONG AS YOU KERP THE LOGO DESIGN. YOU MAY ALSO ADJUST THE LOGO A BIT TO SUIT YOUR DESIGN. - sorry im using capital letters to show importance but im not yelling :)

UPDATE: To clarify, I have uploaded a video called Corvel in the box to show what the current product look like. It is a corvel jar with a logo only and the jar box has a window that shows the jar with the logo on it and the back of that jar box has a bigger version of the label that has more details (i.e. Fragrance name and website link). So to make it clear, I would like to have two versions of the lables: 1. on the jar with minimal info (logo only or logo with the business name) 2. Bigger version of the label with more info to put on the back of the jar box - as described above. The dimensions of the jars are as per this link https://www.lunaxo-example.com.au/corvel-medium-base-and-flat-lid-amber-packed-with-lid-on/ The dimensions of the jar box as per this link https://www.lunaxo-example.com.au/corvel-medium-flat-lid-candle-box-with-window-beige/ Looking forward to some artistic productions :)

Update #2: Tues 25 Dec 18 1. I have uploaded the photo which has the logo with the name 'Silken Meadow' below it just for a reference. However, I would like the designer to modify the current font and NOT to use it as the word 'of in the phrase 'Silken Meadow' does not come out clear enough after printing. 2. I would like the designer NOT to create a design that will require a clear sticker/label for printing. 3. I have attached the photos of my current designs on the jars or the jar box just as a reference but please do NOT just use the same fonts and only change background. I am hoping to see something different and more professional than my own design :) Thank you very much!

Font styles to use
Decorative
Script

Requirements
Must have
• I would like them to fit on the three colors of the jars below - white, amber and black. Below is a link to how the jar looks like https://www.lunaxo-example.com.au/candle-making-supplies/candle-jars/corvel-candle-jars/?glassware_colour=415,443,417&glassware_size=268
Nice to have
• I would like to have a modern design which is suitable for both feminine and musculine.
Should not have
• shouldnt have so much writing on it!

```html
<!DOCTYPE html>
<html lang="en">
<head>
<meta charset="utf-8">
<title>Silken Meadow – Candle Label and Gift Box Dieline</title>
<link href="https://fonts.googleapis.com/css2?family=Cinzel:wght@500&family=Montserrat:wght@500&display=swap" rel="stylesheet">
<style>
  :root {
    --paper: #ffffff;
    --ink: #1c1a17;
    --rule: #b9b9b9;
    --gold-light: #fbefb4;
    --gold-mid: #e2c25c;
    --gold-deep: #b58a26;
    --gold-edge: #c9a13e;
  }
  * { margin: 0; padding: 0; box-sizing: border-box; }
  html, body { width: 1200px; height: 1199px; overflow: hidden; background: var(--paper); }
  .canvas { position: relative; width: 1200px; height: 1199px; background: var(--paper); }

  .seal {
    position: absolute;
    border-radius: 50%;
    background: linear-gradient(135deg, var(--gold-deep) 0%, var(--gold-light) 35%, var(--gold-mid) 60%, var(--gold-deep) 100%);
    box-shadow: inset 0 0 0 3px var(--gold-edge);
    display: flex; flex-direction: column; align-items: center; justify-content: center;
    font-family: "Cinzel", serif; font-weight: 500; color: var(--ink);
    line-height: 1.05; text-align: center;
  }
  .seal--flipped { transform: rotate(180deg); }

  .jar-label { left: 450px; top: 90px; width: 300px; height: 300px; font-size: 44px; }

  .dieline { position: absolute; left: 58px; top: 520px; width: 1084px; height: 583px; }
  .panel { position: absolute; border: 1px solid var(--rule); background: var(--paper); }
  .panel--lid { left: 0; top: 0; width: 274px; height: 223px; border-bottom: none; border-radius: 0 18px 0 0; }
  .panel--front { left: 0; top: 222px; width: 274px; height: 361px; }
  .panel--side-a { left: 273px; top: 222px; width: 269px; height: 361px; }
  .panel--window { left: 541px; top: 222px; width: 275px; height: 361px; }
  .panel--side-b { left: 815px; top: 222px; width: 269px; height: 361px; }

  .panel .seal { left: 50%; margin-left: calc(var(--d) / -2); width: var(--d); height: var(--d); }

  .fragrance {
    position: absolute; left: 0; right: 0; text-align: center;
    font-family: "Cinzel", serif; font-weight: 500; font-size: 19px; color: var(--ink); letter-spacing: 0.5px;
  }
  .contact {
    position: absolute; left: 0; right: 0; text-align: center;
    font-family: "Montserrat", sans-serif; font-weight: 500; font-size: 8.5px; color: var(--ink); line-height: 1.5;
  }
  .contact__web { letter-spacing: 3px; }
  .wordmark-small {
    position: absolute; left: 0; right: 0; top: 12px; text-align: center;
    font-family: "Cinzel", serif; font-weight: 500; font-size: 13px; color: var(--ink);
  }
  .window-cutout {
    position: absolute; left: 44px; top: 38px; width: 187px; height: 277px;
    border: 1px solid var(--rule);
  }
</style>
</head>
<body>
<main class="canvas">
  <div class="seal jar-label">
    <span>SILKEN</span><span>MEADOW</span>
  </div>

  <section class="dieline">
    <div class="panel panel--lid">
      <div class="seal seal--flipped" style="--d:112px; top:55px; font-size:15px;">
        <span>SILKEN</span><span>MEADOW</span>
      </div>
    </div>

    <div class="panel panel--front">
      <div class="seal" style="--d:160px; top:47px; font-size:23px;">
        <span>SILKEN</span><span>MEADOW</span>
      </div>
      <p class="fragrance" style="top:229px;">TURKISH ROSE</p>
      <div class="contact" style="top:310px;">
        <p>+61 491 570 156 &nbsp; | &nbsp; hello@silkenmeadow.com.au</p>
        <p class="contact__web">www.silkenmeadow.com.au</p>
      </div>
    </div>

    <div class="panel panel--side-a">
      <div class="seal" style="--d:155px; top:103px; font-size:22px;">
        <span>SILKEN</span><span>MEADOW</span>
      </div>
    </div>

    <div class="panel panel--window">
      <p class="wordmark-small">SILKEN MEADOW</p>
      <div class="window-cutout"></div>
      <p class="fragrance" style="top:324px;">TURKISH ROSE</p>
    </div>

    <div class="panel panel--side-b">
      <div class="seal" style="--d:155px; top:103px; font-size:22px;">
        <span>SILKEN</span><span>MEADOW</span>
      </div>
    </div>
  </section>
</main>
</body>
</html>
```